Kerno Solutions: searching for a flyer to trow in letterboxes for properties we are interested in

Hello ,

Introduction:
We are a company based in Luxembourg called "Kerno Solutions". We are specialized in buying properties on which we develop and build constructions before selling them.

Informations for the flyer:
We need a flyer to trow into the letter boxes of property owners letting them know that we are interested in buying their property, if they are interested they can give us a call.

The text for the flyer/letter is in the attachment called >>2020-03-11_KS_Text for flyer,letter there might be slight changes<<.

We need to look competent, professional and financially stable.

The flyer needs to be short and not over welling with information otherwise it will land in the trash.

We have decided that we don't want real pictures on the flyer, but shapes of any kind, blue prints, drawings are fine.

Format should be in DIN A4. We plan to print the flyer on both sides in two different languages, in other words the design will be the same on both sides only the text will be in a different language.

I also added our current logo and here is the design of the website that is under construction at the moment http://www.kernosolutions-example.lu/. The logo's color can be changed into a different blue or uni color (all white or all black).
Updates

Hi, First time user the howl thing started faster as expected. Furthermore, I need to catch my boss to discust the project with him and he is on a lot of meetings. Please give us a little bit more time. Thanks

Target Market(s)

Property owners

Requirements
Must have
• email, phone number, tax number (RCS), Tax number , matriculation and address.
see word file in attachment for information
Nice to have
• Our company logo, in one form or an other, you can be creative, the logo is in the attachment.
Should not have
• Real pictures

```html
<!DOCTYPE html>
<html lang="fr">
<head>
<meta charset="utf-8">
<title>Kerno Solutions – Flyer A4</title>
<link rel="stylesheet" href="https://fonts.googleapis.com/css2?family=Source+Sans+3:wght@400;600;700&display=swap">
<style>
  :root {
    --backdrop: #e7e8e6;
    --paper: #ffffff;
    --ink: #1a1a1a;
    --brand-navy: #1d5f8c;
    --accent-blue: #18a6e4;
    --plan-blue: #00a7e8;
  }
  * { box-sizing: border-box; margin: 0; padding: 0; }
  html, body { width: 1200px; height: 848px; overflow: hidden; }
  body {
    background: var(--backdrop);
    font-family: "Source Sans 3", "Myriad Pro", sans-serif;
    color: var(--ink);
    position: relative;
  }
  .sheet {
    position: absolute;
    top: 84px;
    width: 490px;
    height: 687px;
    background: var(--paper);
    overflow: hidden;
  }
  .sheet--lb { left: 86px; }
  .sheet--fr { left: 616px; }

  .plan-backdrop {
    position: absolute;
    left: 0; right: 0; bottom: 0;
    height: 330px;
    background: linear-gradient(180deg,
      rgba(0,167,232,0) 0%,
      rgba(0,167,232,0.08) 18%,
      rgba(0,167,232,0.55) 42%,
      var(--plan-blue) 70%,
      var(--plan-blue) 100%);
  }

  .brand {
    position: absolute;
    right: 62px;
    top: 84px;
    display: flex;
    align-items: center;
    gap: 6px;
    font-weight: 700;
    font-size: 17px;
    letter-spacing: 0.3px;
    color: var(--brand-navy);
    text-transform: uppercase;
  }
  .brand__mark {
    width: 12px; height: 12px;
    background: var(--brand-navy);
  }

  .letter {
    position: absolute;
    left: 58px;
    top: 108px;
    width: 380px;
    font-size: 9.2px;
    line-height: 11.5px;
  }
  .letter__greeting { font-weight: 700; font-size: 10px; margin-bottom: 11.5px; }
  .letter p { margin-bottom: 11.5px; }
  .letter__sign { margin-top: 0; }
  .letter__sign--spaced { margin-top: 11.5px; }

  .contact {
    position: absolute;
    left: 49px;
    top: 302px;
    font-size: 9.2px;
    line-height: 11.5px;
    list-style: none;
  }
  .contact li { display: flex; align-items: center; }
  .contact__icon {
    width: 9px; height: 9px; flex: none;
    fill: none; stroke: var(--accent-blue); stroke-width: 1.3;
  }
  .contact__spacer { width: 9px; flex: none; }

  .website {
    position: absolute;
    left: 48px;
    top: 363px;
    display: flex;
    align-items: center;
    gap: 1px;
    font-weight: 700;
    font-size: 13.5px;
    color: var(--accent-blue);
    text-decoration: none;
  }
  .website svg { width: 10px; height: 10px; fill: none; stroke: var(--accent-blue); stroke-width: 1.1; }
</style>
</head>
<body>

<svg width="0" height="0" style="position:absolute">
  <defs>
    <symbol id="icon-pin" viewBox="0 0 10 10"><path d="M5 9.3 C3 6.6 2.2 5.2 2.2 3.8 a2.8 2.8 0 0 1 5.6 0 C7.8 5.2 7 6.6 5 9.3Z"/><circle cx="5" cy="3.8" r="1"/></symbol>
    <symbol id="icon-mail" viewBox="0 0 10 10"><rect x="1" y="2.5" width="8" height="5.4"/><path d="M1 2.5 L5 5.8 L9 2.5"/></symbol>
    <symbol id="icon-phone" viewBox="0 0 10 10"><path d="M3 1.2 L4.3 3.4 L3.4 4.3 C3.9 5.6 4.6 6.4 5.8 6.9 L6.7 6 L8.8 7.3 L8 8.7 C5 8.7 1.4 5.2 1.6 2 Z"/></symbol>
    <symbol id="icon-globe" viewBox="0 0 10 10"><circle cx="5" cy="5" r="4"/><ellipse cx="5" cy="5" rx="1.8" ry="4"/><path d="M1 5 H9 M1.6 3 H8.4 M1.6 7 H8.4"/></symbol>
  </defs>
</svg>

<!-- Luxembourgish side -->
<section class="sheet sheet--lb" lang="lb">
  <div class="plan-backdrop" role="img" aria-label="Faded architectural floor plan drawing fading into blue"></div>
  <div class="brand"><span class="brand__mark"></span>Kerno Solutions</div>

  <div class="letter">
    <p class="letter__greeting">Madame, Monsieur,</p>
    <p>Dir kritt dëst Schreiwes well Är Proprietéit eis Opmierksamkeet zeréckbehalen huet.<br>
    Mir géinge gär mat Iech iwwert d’Méiglechkeet, datt eise Betrib se opkeeft, diskutéieren.</p>
    <p>Mir versécheren Iech e séieren Entscheedungsprozess, garantéieren d’Bezuelung a verrechne keng Drëttkäschten.</p>
    <p>Mir géingen eis freeën, vun Iech ze héieren, a sti ganz zu Ärer Verfügung fir zousätzlech Informatiounen.</p>
    <p>Mat beschte Gréiss,</p>
    <p class="letter__sign">D’Equipe vun Kerno Solutions</p>
  </div>

  <ul class="contact">
    <li><span class="contact__spacer"></span>Company name : Kerno Solutions sàrl</li>
    <li><svg class="contact__icon"><use href="#icon-pin"/></svg>Address : 17 rue des Artisans, L-4321 Esch-Village</li>
    <li><svg class="contact__icon"><use href="#icon-mail"/></svg>Email: info@kernosolutions-example.lu</li>
    <li><svg class="contact__icon"><use href="#icon-phone"/></svg>Tel. : 691 000 555</li>
    <li><span class="contact__spacer"></span>RCS :</li>
  </ul>

  <a class="website" href="http://www.kernosolutions-example.lu/"><svg><use href="#icon-globe"/></svg>www.kernosolutions-example.lu</a>
</section>

<!-- French side -->
<section class="sheet sheet--fr" lang="fr">
  <div class="plan-backdrop" role="img" aria-label="Plan d’architecte estompé se fondant dans le bleu"></div>
  <div class="brand"><span class="brand__mark"></span>Kerno Solutions</div>

  <div class="letter">
    <p class="letter__greeting">Madame, Monsieur,</p>
    <p>Ce courrier vous a été adressé, car votre propriété a attiré notre attention. Nous souhaiterions discuter avec vous de son éventuel rachat par notre société.</p>
    <p>En cas d’accord, nous vous assurons une décision rapide, un paiement garanti, et zéro frais d’intermédiaire.</p>
    <p>En attendant de vos nouvelles, nous restons à votre entière disposition pour tout renseignement.</p>
    <p>Salutations distinguées,</p>
    <p class="letter__sign letter__sign--spaced">L’équipe de Kerno Solutions</p>
  </div>

  <ul class="contact">
    <li><span class="contact__spacer"></span>Company name : Kerno Solutions sàrl</li>
    <li><svg class="contact__icon"><use href="#icon-pin"/></svg>Address : 17 rue des Artisans, L-4321 Esch-Village</li>
    <li><svg class="contact__icon"><use href="#icon-mail"/></svg>Email: info@kernosolutions-example.lu</li>
    <li><svg class="contact__icon"><use href="#icon-phone"/></svg>Tel. : 691 000 555</li>
    <li><span class="contact__spacer"></span>RCS :</li>
  </ul>

  <a class="website" href="http://www.kernosolutions-example.lu/"><svg><use href="#icon-globe"/></svg>www.kernosolutions-example.lu</a>
</section>

</body>
</html>
```